Healthcare patient advocacy company needs banner for conference booth

We need a banner to hang behind us in our booth at conferences. I would like something that prominently features our company name - velorin LLC. And also includes the following language: No employee should face medical debt alone. No Plan should be unrepresented. Expert advocacy and legal support from first bill to final resolution. The colors we use for our other materials are HEX 002C45, FECC73, 00C6CF, E0D5B9, 004C66. And the font is Epilogue. I would welcome some graphics, but no scales of justice or dollar bills or anything like that. I'm attaching some materials so you can see one of our brochures.

Target Market(s)

B2B - health insurers, third-party health care administrators, cost-containment companies

Industry/Entity Type

Healthcare Advocacy

Requirements
Must have
• Name prominently displayed and taglines in project description.
Nice to have
• I would like something easy to read and eye-catching that is not overly complicated or cutsey.
Should not have
• Scales of justice or dollar signs.

```html
<!DOCTYPE html>
<html lang="en">
<head>
<meta charset="utf-8">
<title>velorin LLC — Conference Booth Banner</title>
<link href="https://fonts.googleapis.com/css2?family=Epilogue:wght@300;400;700;800&display=swap" rel="stylesheet">
<style>
  :root {
    --navy: #002C45;
    --navy-deep: #001a2b;
    --gold: #FECC73;
    --teal: #00C6CF;
    --sand: #E0D5B9;
    --petrol: #004C66;
    --white: #ffffff;
  }
  * { margin: 0; padding: 0; box-sizing: border-box; }
  html, body {
    width: 1200px;
    height: 840px;
    overflow: hidden;
    background: var(--navy);
  }
  .banner {
    position: relative;
    width: 1200px;
    height: 840px;
    background: linear-gradient(160deg, var(--navy) 0%, var(--navy) 55%, var(--navy-deep) 100%);
    font-family: "Epilogue", sans-serif;
    color: var(--white);
    overflow: hidden;
  }
  .brand {
    position: absolute;
    left: 64px;
    top: 58px;
    display: flex;
    align-items: center;
    gap: 22px;
  }
  .brand-name {
    font-weight: 700;
    font-size: 62px;
    letter-spacing: -0.5px;
    color: var(--gold);
    line-height: 1;
  }
  .brand-dot {
    width: 40px;
    height: 40px;
    border-radius: 50%;
    background: var(--gold);
  }
  .headline {
    position: absolute;
    left: 64px;
    top: 168px;
    font-weight: 800;
    font-size: 46px;
    line-height: 1.2;
    letter-spacing: -0.5px;
  }
  .headline .accent { color: var(--teal); display: block; }
  .headline .plain { color: var(--white); display: block; }
  .divider {
    position: absolute;
    left: 66px;
    top: 372px;
    display: flex;
    gap: 6px;
  }
  .divider span {
    height: 6px;
    border-radius: 3px;
    background: var(--teal);
  }
  .divider .long { width: 48px; }
  .divider .short { width: 10px; background: var(--white); }
  .pledges {
    position: absolute;
    left: 64px;
    top: 400px;
    list-style: none;
    display: flex;
    flex-direction: column;
    gap: 26px;
  }
  .pledge {
    display: flex;
    align-items: center;
    gap: 16px;
  }
  .pledge-icon {
    width: 54px;
    height: 54px;
    flex: none;
  }
  .pledge-text {
    font-weight: 300;
    font-size: 26px;
    line-height: 1.2;
    color: var(--white);
  }
  .site {
    position: absolute;
    left: 64px;
    top: 720px;
    font-weight: 400;
    font-size: 34px;
    color: var(--white);
  }
  .site .domain { color: var(--teal); }
  .pattern-column {
    position: absolute;
    left: 930px;
    top: 28px;
    width: 214px;
    height: 784px;
  }
</style>
</head>
<body>
<main class="banner">
  <header class="brand">
    <h1 class="brand-name">velorin LLC</h1>
    <span class="brand-dot" aria-hidden="true"></span>
  </header>

  <h2 class="headline">
    <span class="accent">Protecting patients,</span>
    <span class="accent">health plans and insurers</span>
    <span class="plain">across the U.S.</span>
  </h2>

  <div class="divider" aria-hidden="true">
    <span class="long"></span><span class="short"></span>
  </div>

  <ul class="pledges">
    <li class="pledge">
      <svg class="pledge-icon" viewBox="0 0 54 54" aria-hidden="true">
        <circle cx="27" cy="27" r="27" fill="var(--teal)"/>
        <circle cx="27" cy="21" r="7" fill="none" stroke="var(--navy)" stroke-width="2.5"/>
        <path d="M14 40c2-7 7-10 13-10s11 3 13 10" fill="none" stroke="var(--navy)" stroke-width="2.5" stroke-linecap="round"/>
      </svg>
      <p class="pledge-text">No employee should<br>face medical debt alone.</p>
    </li>
    <li class="pledge">
      <svg class="pledge-icon" viewBox="0 0 54 54" aria-hidden="true">
        <circle cx="27" cy="27" r="27" fill="var(--teal)"/>
        <rect x="17" y="13" width="20" height="27" rx="2" fill="none" stroke="var(--navy)" stroke-width="2.5"/>
        <path d="M27 19v8M23 23h8M21 32h12M21 36h8" stroke="var(--navy)" stroke-width="2.5" stroke-linecap="round"/>
      </svg>
      <p class="pledge-text">No Plan should be<br>unrepresented.</p>
    </li>
    <li class="pledge">
      <svg class="pledge-icon" viewBox="0 0 54 54" aria-hidden="true">
        <circle cx="27" cy="27" r="27" fill="var(--teal)"/>
        <path d="M27 12l12 5v9c0 8-5 13-12 16-7-3-12-8-12-16v-9z" fill="none" stroke="var(--navy)" stroke-width="2.5" stroke-linejoin="round"/>
        <path d="M21 27l4 4 8-8" fill="none" stroke="var(--navy)" stroke-width="2.5" stroke-linecap="round" stroke-linejoin="round"/>
      </svg>
      <p class="pledge-text">Expert advocacy and legal support<br>from first bill to final resolution.</p>
    </li>
  </ul>

  <p class="site"><span class="domain">velorinhealth</span>.com</p>

  <svg class="pattern-column" viewBox="0 0 214 784" role="img" aria-label="Decorative column of geometric shapes in teal, gold, sand and petrol">
    <defs>
      <linearGradient id="columnTones" x1="0" y1="0" x2="0" y2="1">
        <stop offset="0" stop-color="#00C6CF"/>
        <stop offset="0.3" stop-color="#E0D5B9"/>
        <stop offset="0.5" stop-color="#FECC73"/>
        <stop offset="0.75" stop-color="#004C66"/>
        <stop offset="1" stop-color="#00C6CF"/>
      </linearGradient>
    </defs>
    <rect width="214" height="784" rx="6" fill="url(#columnTones)"/>
  </svg>
</main>
</body>
</html>
```